Humming Lanterns Parlour Business Card plus one change to logo design

Hi Ingrid,

OK I am ready to get a business card designed. It should have following on front

Logo
Delia Forbrook-Vane
Founder

e: delia@humminglanternsparlour.example
w: www.humminglanternsparlour.example
c: 555-218-4796

On Back:

Humming Lanterns Parlour is currently looking for contributors, supporting enterprises, and members-if interested, please get in touch!

I would also like you to change the byline to "for progressive minds with bold ideas"

```html
<!DOCTYPE html>
<html lang="en">
<head>
<meta charset="utf-8">
<title>Humming Lanterns Parlour – Business Card</title>
<link rel="stylesheet" href="https://fonts.googleapis.com/css2?family=Ubuntu:wght@400;500;700&display=swap">
<style>
  :root {
    --page: #ffffff;
    --card-front: #ffffff;
    --card-border: #b9b9b9;
    --card-back: #2d2d2d;
    --ink: #3a3a3a;
    --ink-soft: #5a5a5a;
    --accent: #b0222a;
    --on-dark: #ffffff;
  }
  * { margin: 0; padding: 0; box-sizing: border-box; }
  html, body { width: 867px; height: 1200px; overflow: hidden; background: var(--page); }
  body { position: relative; font-family: "Ubuntu", Arial, sans-serif; color: var(--ink); }

  .side-label {
    position: absolute; left: 0; width: 867px; text-align: center;
    font-size: 24px; color: var(--ink-soft); white-space: pre;
  }
  .side-label--front { top: 2px; }
  .side-label--back { top: 600px; }

  .card { position: absolute; left: 6px; width: 855px; border-radius: 26px; overflow: hidden; }
  .card--front { top: 40px; height: 538px; background: var(--card-front); border: 2px solid var(--card-border); }
  .card--back { top: 641px; height: 549px; background: var(--card-back); }

  .brand { position: absolute; left: 170px; top: 110px; width: 520px; }
  .brand__row { display: flex; align-items: center; gap: 16px; }
  .brand__dot { width: 34px; height: 34px; border-radius: 50%; background: var(--accent); flex: none; }
  .brand__name { font-size: 40px; font-weight: 700; color: var(--ink); letter-spacing: -0.5px; white-space: nowrap; }
  .brand__byline { margin-top: 10px; margin-left: 50px; font-size: 19px; color: var(--accent); letter-spacing: 0.5px; }

  .person { position: absolute; left: 0; width: 855px; top: 268px; text-align: center; }
  .person__name { font-size: 28px; font-weight: 700; color: var(--ink); letter-spacing: 0.5px; }
  .person__role { margin-top: 6px; font-size: 20px; color: var(--ink-soft); }

  .contact { position: absolute; left: 0; width: 855px; top: 382px; text-align: center; list-style: none; }
  .contact li { font-size: 20px; color: var(--ink); line-height: 40px; }

  .back-mark { position: absolute; left: 42px; top: 290px; width: 70px; height: 70px; border-radius: 50%; background: var(--accent); }
  .back-message {
    position: absolute; left: 292px; top: 286px; width: 520px;
    font-size: 27px; font-weight: 500; line-height: 43px; color: var(--on-dark);
  }
</style>
</head>
<body>
  <div class="side-label side-label--front">Front side    Opt3</div>

  <section class="card card--front">
    <div class="brand">
      <div class="brand__row">
        <span class="brand__dot"></span>
        <span class="brand__name">Humming Lanterns Parlour</span>
      </div>
      <p class="brand__byline">for progressive minds with bold ideas</p>
    </div>

    <div class="person">
      <p class="person__name">Delia Forbrook-Vane</p>
      <p class="person__role">Founder</p>
    </div>

    <ul class="contact">
      <li>c: 555-218-4796</li>
      <li>e: delia@humminglanternsparlour.example</li>
      <li>w: www.humminglanternsparlour.example</li>
    </ul>
  </section>

  <div class="side-label side-label--back">Back side    Opt3</div>

  <section class="card card--back">
    <span class="back-mark"></span>
    <p class="back-message">Humming Lanterns Parlour is currently looking for contributors, supporting enterprises, and members-if interested, please get in touch!</p>
  </section>
</body>
</html>
```